GHollis Busisness Card

I am an aerospace consultant and at this time only need business cards.

Industry/Entity Type

Business

Contact Information for Business Card

Hollis Partners,LLC
Gerald T. Hollis

348 Birch Hollow Road
Madison AL 35762

256-555-0148 (cell)
256-555-0173 (fax)

geraldhollis@mailbrook.net

```html
<!DOCTYPE html>
<html lang="en">
<head>
<meta charset="utf-8">
<title>Hollis Partners, LLC — Business Card</title>
<link rel="stylesheet" href="https://fonts.googleapis.com/css2?family=Oxygen:wght@400;700&display=swap">
<style>
  :root {
    --backdrop: #272727;
    --card: #ffffff;
    --ink: #231f20;
    --accent-red: #d71f2a;
    --band-text: #ffffff;
    --soft-grey: rgba(220, 222, 226, 0.75);
    --soft-peach: rgba(246, 214, 200, 0.6);
  }
  * { box-sizing: border-box; margin: 0; padding: 0; }
  html, body {
    width: 1200px;
    height: 900px;
    overflow: hidden;
    background: var(--backdrop);
  }
  .canvas {
    position: relative;
    width: 1200px;
    height: 900px;
  }
  .business-card {
    position: absolute;
    left: 269px;
    top: 266px;
    width: 662px;
    height: 367px;
    background: var(--card);
    overflow: hidden;
    font-family: "Oxygen", "Helvetica Neue", Arial, sans-serif;
  }
  .backdrop-decoration {
    position: absolute;
    left: 290px;
    top: 0;
    width: 380px;
    height: 280px;
    background:
      radial-gradient(ellipse 60% 55% at 70% 45%, var(--soft-grey) 0%, rgba(230, 231, 234, 0.35) 55%, rgba(255, 255, 255, 0) 80%),
      radial-gradient(ellipse 45% 45% at 60% 75%, var(--soft-peach) 0%, rgba(255, 255, 255, 0) 75%);
  }
  .company-mark {
    position: absolute;
    left: 148px;
    top: 160px;
    display: flex;
    align-items: center;
    gap: 18px;
  }
  .company-mark__square {
    width: 26px;
    height: 26px;
    background: var(--accent-red);
  }
  .company-mark__name {
    font-weight: 700;
    font-size: 34px;
    line-height: 44px;
    color: var(--ink);
    letter-spacing: -0.4px;
    white-space: nowrap;
  }
  .person-name {
    position: absolute;
    left: 0;
    right: 0;
    top: 246px;
    text-align: center;
    font-size: 21px;
    line-height: 28px;
    font-weight: 400;
    color: var(--ink);
    letter-spacing: 0.3px;
  }
  .contact-band {
    position: absolute;
    left: 0;
    right: 0;
    bottom: 0;
    height: 46px;
    background: var(--accent-red);
    display: flex;
    align-items: center;
    justify-content: center;
  }
  .contact-band__line {
    color: var(--band-text);
    font-size: 13.4px;
    white-space: nowrap;
    letter-spacing: -0.2px;
  }
</style>
</head>
<body>
  <div class="canvas">
    <section class="business-card">
      <div class="backdrop-decoration" role="img" aria-label="Faint sweeping grey and peach arcs in the background"></div>
      <div class="company-mark">
        <span class="company-mark__square"></span>
        <span class="company-mark__name">Hollis Partners,LLC</span>
      </div>
      <p class="person-name">Gerald T. Hollis</p>
      <footer class="contact-band">
        <p class="contact-band__line">348 Birch Hollow Road Madison AL 35762 256-555-0148 (cell) 256-555-0173 (fax) geraldhollis@mailbrook.net</p>
      </footer>
    </section>
  </div>
</body>
</html>
```